Refresh of The Marston Collective business card

Update business card design using existing primary logo. Names, numbers, etc. are too hard to read on current design.

Target Market(s)

We are a CPA firm.

Industry/Entity Type

Accountant

Contact Information for Business Card

update current card

Colors
0355a3
3176b5
85acd3
0792cd

Requirements
Must have
• Easier to read phone numbers and names
• Use existing logo
Nice to have
• We love our color scheme and current TMC logo. But the names and phone numbers are too small and card just look old and stale.

```html
<!DOCTYPE html>
<html lang="en">
<head>
<meta charset="utf-8">
<title>The Marston Collective – Business Card</title>
<link rel="stylesheet" href="https://fonts.googleapis.com/css2?family=EB+Garamond:wght@500;600&family=Montserrat:wght@500&display=swap">
<style>
  :root {
    --brand-blue: #0355a3;
    --brand-mid: #3176b5;
    --brand-light: #85acd3;
    --brand-cyan: #0792cd;
    --paper: #f4f5f7;
    --charcoal: #2c2c2e;
    --charcoal-deep: #222224;
    --stage: #3a3a3c;
    --ink-light: #eef3fa;
    --ink-grey: #d8d8d8;
  }
  * { box-sizing: border-box; margin: 0; padding: 0; }
  html, body { width: 1200px; height: 997px; overflow: hidden; }
  body {
    background: var(--stage);
    font-family: "EB Garamond", Georgia, serif;
    position: relative;
  }
  .card {
    position: absolute;
    left: 250px;
    width: 700px;
    height: 400px;
    overflow: hidden;
    box-shadow: 0 10px 30px rgba(0,0,0,.45);
  }

  /* Back of card */
  .card-back {
    top: 78px;
    background: linear-gradient(135deg, var(--charcoal) 0%, var(--charcoal-deep) 100%);
    display: flex;
    flex-direction: column;
    align-items: center;
    justify-content: center;
    gap: 34px;
  }
  .card-back .lockup { color: var(--ink-grey); }
  .card-back .lockup-mark { border-color: var(--ink-grey); }
  .card-back .website {
    color: var(--ink-grey);
    font-size: 24px;
    letter-spacing: 3px;
  }

  /* Logo lockup */
  .lockup {
    display: flex;
    align-items: center;
    gap: 22px;
  }
  .lockup-mark {
    width: 92px;
    height: 92px;
    border-radius: 50%;
    border: 4px solid currentColor;
    flex: none;
  }
  .lockup-text { display: flex; flex-direction: column; gap: 6px; }
  .lockup-name {
    font-size: 38px;
    font-weight: 600;
    letter-spacing: 1px;
    line-height: 1;
  }
  .lockup-tagline {
    font-family: "Montserrat", Arial, sans-serif;
    font-weight: 500;
    font-size: 11px;
    letter-spacing: 3.5px;
    text-transform: uppercase;
  }

  /* Front of card */
  .card-front {
    top: 518px;
    background: var(--paper);
  }
  .front-head {
    height: 168px;
    display: flex;
    align-items: center;
    justify-content: center;
    color: var(--brand-blue);
  }
  .front-head .lockup-mark { background: var(--brand-blue); border-color: #1b2f4d; }
  .front-rules {
    height: 14px;
    border-top: 3px solid var(--brand-blue);
    border-bottom: 3px solid var(--brand-blue);
    margin-bottom: 4px;
  }
  .front-body {
    height: 214px;
    background: linear-gradient(180deg, var(--brand-blue) 0%, #034a8f 100%);
    display: grid;
    grid-template-columns: 1fr 1px 1fr;
    align-items: center;
    padding: 0 40px;
    color: var(--ink-light);
  }
  .divider { height: 150px; background: var(--brand-light); }
  .contact-list { list-style: none; display: flex; flex-direction: column; gap: 10px; padding-left: 30px; }
  .contact-item { display: flex; align-items: center; gap: 14px; font-size: 21px; }
  .contact-item svg { width: 18px; height: 18px; fill: var(--brand-light); flex: none; }
  .person { padding-left: 40px; }
  .person-name {
    font-size: 24px;
    font-weight: 600;
    letter-spacing: 1px;
    text-transform: uppercase;
    margin-bottom: 26px;
  }
  .person-address { font-size: 21px; line-height: 1.35; font-style: normal; }
</style>
</head>
<body>

<section class="card card-back">
  <div class="lockup">
    <div class="lockup-mark"></div>
    <div class="lockup-text">
      <span class="lockup-name">The Marston Collective</span>
      <span class="lockup-tagline">Certified Public Accountants</span>
    </div>
  </div>
  <p class="website">www.marstoncollective.com</p>
</section>

<section class="card card-front">
  <header class="front-head">
    <div class="lockup">
      <div class="lockup-mark"></div>
      <div class="lockup-text">
        <span class="lockup-name">The Marston Collective</span>
        <span class="lockup-tagline">Certified Public Accountants</span>
      </div>
    </div>
  </header>
  <div class="front-rules"></div>
  <div class="front-body">
    <ul class="contact-list">
      <li class="contact-item">
        <svg viewBox="0 0 24 24" aria-hidden="true"><path d="M3 8c0-2 4-4 9-4s9 2 9 4v2h-5V8H8v2H3z M6 12h12l2 8H4z"/></svg>
        555.210.4387
      </li>
      <li class="contact-item">
        <svg viewBox="0 0 24 24" aria-hidden="true"><path d="M7 3h10v5H7z M3 9h18v8h-3v-3H6v3H3z M6 15h12v6H6z"/></svg>
        555.210.4390
      </li>
      <li class="contact-item">
        <svg viewBox="0 0 24 24" aria-hidden="true"><path d="M7 1h10a2 2 0 0 1 2 2v18a2 2 0 0 1-2 2H7a2 2 0 0 1-2-2V3a2 2 0 0 1 2-2zm0 3v15h10V4z"/></svg>
        555.862.1174
      </li>
      <li class="contact-item">
        <svg viewBox="0 0 24 24" aria-hidden="true"><path d="M2 5h20v14H2z M3 6l9 7 9-7" stroke="#034a8f" stroke-width="1.5"/></svg>
        dan@marstoncollective.com
      </li>
    </ul>
    <div class="divider"></div>
    <div class="person">
      <h1 class="person-name">Daniel R. Whitford, CPA</h1>
      <address class="person-address">318 Lakeview Ave. Suite 104<br>Cedar Glen, Florida 32000</address>
    </div>
  </div>
</section>

</body>
</html>
```